Add Responsiveness to Current Website

The website http://www.velvet-screen-room-studio.example needs to be made responsive. This includes all the menus and all the galleries. The Design, graphics, colors can remain the same, except I can provide larger images and design for the Home Page. If you know what you are doing, this should not take too long.

Coding

Coded - Design and coding required

Number of Pages Required

5+ page

Font styles to use
Sans Serif

Colors
f37122
f78f20

Requirements
Must have
• Responsive Menus and Galleries

```html
<!DOCTYPE html>
<html lang="en">
<head>
<meta charset="utf-8">
<title>Velvet Screen – Home Theater Art and Design</title>
<link rel="stylesheet" href="https://fonts.googleapis.com/css2?family=Oswald:wght@300;400&family=Open+Sans:wght@400;600&display=swap">
<style>
:root{
  --orange:#e8692a;
  --orange-dark:#c4521c;
  --gold:#b8912c;
  --charcoal:#2b2522;
  --nav-dark:#2e2e2e;
  --footer:#2f2823;
  --footer-bottom:#231d19;
  --text:#444;
  --muted:#8a817a;
  --navy:#1f2a5a;
  --line:#e4e4e4;
}
*{margin:0;padding:0;box-sizing:border-box}
html,body{width:667px;height:1200px;overflow:hidden;background:#fff}
body{position:relative;font-family:"Open Sans",Arial,sans-serif;color:var(--text)}
.abs{position:absolute}
.head{font-family:"Oswald",Arial,sans-serif;font-weight:300}

.brand{left:54px;top:20px;font-family:"Oswald",Arial,sans-serif;font-weight:400;font-size:27px;color:var(--gold);display:flex;align-items:center;gap:8px}
.brand-dot{width:14px;height:14px;border-radius:50%;background:var(--gold)}
.contact-top{left:480px;top:20px;display:flex;gap:14px;align-items:flex-start}
.contact-top .lines{font-size:9px;line-height:14px;color:#555}
.contact-top .toll{color:var(--navy)}

.nav-band{left:0;top:72px;width:667px;height:30px;background:var(--nav-dark)}
.nav{left:206px;top:67px;width:407px;height:35px;background:var(--orange);display:flex;align-items:center;justify-content:space-around;padding:4px 6px 0}
.nav a{font-family:"Oswald",Arial,sans-serif;font-weight:300;font-size:9.5px;color:#fff;text-decoration:none}

.hero{left:0;top:102px;width:667px;height:300px;background:linear-gradient(100deg,#6e6430 0%,#8b7d3c 30%,#4a3520 55%,#2b1d12 75%,#6a4422 100%)}
.hero-caption{left:398px;top:200px;color:#fff;width:210px}
.hero-caption h1{font-family:"Oswald",Arial,sans-serif;font-weight:400;font-size:38px;line-height:40px}
.hero-caption h2{font-family:"Oswald",Arial,sans-serif;font-weight:300;font-size:24px;line-height:30px}
.hero-caption p{font-size:7px;line-height:12.5px;margin-top:6px}
.arrow{top:256px;width:18px;height:18px;border-radius:50%;background:rgba(0,0,0,.35)}

.features{left:0;top:402px;width:667px;height:99px;background:var(--orange)}
.feature{top:22px;display:flex;gap:10px;color:#fff;width:190px}
.feature .ic{flex:none;width:28px;height:28px;border:1px solid rgba(255,255,255,.8);border-radius:50%;display:flex;align-items:center;justify-content:center}
.feature h3{font-family:"Oswald",Arial,sans-serif;font-weight:300;font-size:11px;margin-bottom:5px}
.feature p{font-size:6.2px;line-height:11.5px}

.section-title{left:0;width:667px;text-align:center;font-family:"Oswald",Arial,sans-serif;font-weight:300;color:var(--orange)}
.section-sub{left:0;top:546px;width:667px;text-align:center;font-size:8px;color:#333}
.divider{left:55px;width:557px;height:1px;background:var(--line)}
.divider i{position:absolute;left:274px;top:-3px;width:7px;height:7px;transform:rotate(45deg);border:1px solid #ccc;background:#fff}

.card{top:594px;width:134px;height:166px}
.card .photo{height:138px;display:flex;justify-content:center;align-items:center;gap:4px}
.card .tools span{display:inline-block;width:20px;height:20px;border-radius:50%;background:rgba(0,0,0,.55);border:1px solid #999;margin:0 2px}
.card .cap{height:28px;background:var(--gold);font-family:"Oswald",Arial,sans-serif;font-weight:300;font-size:9px;color:#fff;padding:9px 9px}

.reasons-photo{left:55px;top:824px;width:143px;height:154px;background:linear-gradient(160deg,#5a4d4a,#2c2220 60%,#15110f)}
.reasons-title{left:216px;top:824px;font-family:"Oswald",Arial,sans-serif;font-weight:300;font-size:14px;color:#444}
.reason{width:125px}
.reason h4{font-size:8px;font-weight:400;color:var(--orange);display:flex;align-items:center;gap:4px;margin-bottom:3px}
.reason h4 b{width:12px;height:12px;border:1px solid var(--orange);border-radius:50%;font-size:7px;font-weight:400;display:flex;align-items:center;justify-content:center}
.reason p{font-size:5.8px;line-height:12px;color:#333}

.footer{left:0;top:1018px;width:667px;height:147px;background:var(--footer)}
.foot-bottom{left:0;top:1165px;width:667px;height:35px;background:var(--footer-bottom);font-size:6px;color:#aaa;text-align:center;padding-top:15px}
.foot-bottom b{color:#fff;font-weight:600}
.foot-col h5{font-size:8.5px;font-weight:400;color:#bbb;letter-spacing:.3px;margin-bottom:12px}
.foot-col li{list-style:none;font-size:6.5px;color:#bbb;line-height:13.4px}
.review{left:284px;top:1049px;width:190px}
.review .avatar{width:25px;height:25px;background:var(--gold);float:left;margin:0 18px 0 0}
.review .name{font-size:8px;color:#998;margin-bottom:4px}
.review p{font-size:5.6px;line-height:10px;color:#888;margin-left:43px}
.stars{margin:4px 0 0 43px;font-size:6px;color:var(--orange)}
.stars em{font-style:normal;color:#fff}

.contact-box{left:481px;top:1005px;width:121px;height:160px;background:var(--orange);color:#fff;padding:34px 10px 0}
.contact-box h5{font-size:8.5px;font-weight:400;margin-bottom:10px}
.contact-box p{font-size:6.4px;line-height:11px}
.contact-box .row{display:flex;align-items:center;gap:7px;font-size:7px;margin-top:6px}
.socials{display:flex;gap:3px;margin-top:16px}
.socials span{width:13px;height:13px;border:1px solid #fff;border-radius:50%}
.fold{top:1005px;width:0;height:0;border-bottom:8px solid var(--orange-dark)}
</style>
</head>
<body>

<header>
  <div class="abs brand"><span class="brand-dot"></span>Velvet Screen</div>
  <div class="abs contact-top">
    <svg width="16" height="20" viewBox="0 0 16 20"><path d="M3 1l3 0 1 5-2 2c1 3 3 5 5 6l2-2 4 1 0 3c-1 2-3 2-5 1C6 15 2 10 1 5 0 3 1 1 3 1z" fill="#cfcfcf"/></svg>
    <div class="lines">hello@velvetscreen.example<br><span class="toll">Toll Free : 555-214-7730</span></div>
  </div>
</header>

<div class="abs nav-band"></div>
<nav class="abs nav">
  <a href="#">Home</a><a href="#">Products</a><a href="#">Gallery</a><a href="#">Acoustics</a><a href="#">Our Story</a><a href="#">Hospitality</a><a href="#">Seating</a><a href="#">Contact Us</a>
</nav>

<section>
  <div class="abs hero" role="img" aria-label="Home theater room with recliners, framed wall panels and a large screen showing a waterfall"></div>
  <div class="abs arrow" style="left:19px"><svg width="18" height="18"><path d="M10 5l-4 4 4 4" stroke="#ddd" fill="none" stroke-width="1.5"/></svg></div>
  <div class="abs arrow" style="left:629px"><svg width="18" height="18"><path d="M8 5l4 4-4 4" stroke="#ddd" fill="none" stroke-width="1.5"/></svg></div>
  <div class="abs hero-caption">
    <h1>Home Theater</h1>
    <h2>Art and Design</h2>
    <p>Lorem ipsum dolor sit amet, consectetur adipiscing elit, sed tempor incididunt ut labore et dolore magna aliqua. Ut enim ullamco laboris nisi ut aliquip ex ea commodo</p>
  </div>
</section>

<section class="abs features">
  <div class="abs feature" style="left:55px">
    <div class="ic"><svg width="12" height="12" viewBox="0 0 12 12"><circle cx="6" cy="3.5" r="2.5" fill="#fff"/><path d="M1 12c0-4 10-4 10 0z" fill="#fff"/></svg></div>
    <div><h3>Your Personal Consultant</h3><p>The moment you contact Velvet Screen, you will talk directly with Mara Ellison, the President and founder of the company.</p></div>
  </div>
  <div class="abs feature" style="left:247px">
    <div class="ic"><svg width="12" height="12" viewBox="0 0 12 12"><path d="M6 1a5 5 0 100 10c1 0 1-1 .5-2s0-2 1.5-2h2c1 0 1-1 1-1A5 5 0 006 1z" fill="#fff"/></svg></div>
    <div><h3>Custom Panels &amp; Designs</h3><p>Since no two rooms are alike, your theater may require custom sized acoustic panels to establish a proper visual and sound</p></div>
  </div>
  <div class="abs feature" style="left:448px">
    <div class="ic"><svg width="12" height="12" viewBox="0 0 12 12"><path d="M1 4h3l3-3v10L4 8H1z" fill="#fff"/><path d="M9 4c1 1 1 3 0 4" stroke="#fff" fill="none"/></svg></div>
    <div><h3>Sound Control Panels</h3><p>Almost lost in the conversation is the fact that all these beautiful products are actually acoustic panels. When investing</p></div>
  </div>
</section>

<section>
  <h2 class="abs section-title" style="top:516px;font-size:18px">Our Featured Gallery</h2>
  <p class="abs section-sub">We offer an overflowing portfolio of beautiful furnishing s for you</p>
  <div class="abs divider" style="top:571px"><i></i></div>

  <div class="abs card" style="left:55px"><div class="photo tools" role="img" aria-label="Theater room with movie posters and black leather recliners" style="background:linear-gradient(180deg,#1e2a4a,#2a2a30 50%,#111)"><span></span><span></span></div><div class="cap">Home Theater Acoustic Panels</div></div>
  <div class="abs card" style="left:196px"><div class="photo tools" role="img" aria-label="Theater room with sunset wall art and recliners" style="background:linear-gradient(180deg,#3a2e26,#8a4a20 40%,#2a2420)"><span></span><span></span></div><div class="cap">Home Theater Acoustic Panels</div></div>
  <div class="abs card" style="left:336px"><div class="photo tools" role="img" aria-label="Tiered theater seating in a paneled room" style="background:linear-gradient(180deg,#5a3e38,#3a2a22 50%,#1a1412)"><span></span><span></span></div><div class="cap">Home Theater Acoustic Panels</div></div>
  <div class="abs card" style="left:477px"><div class="photo tools" role="img" aria-label="Theater with patterned acoustic wall panels and a recliner" style="background:linear-gradient(180deg,#3a3430,#6a5a48 50%,#2a2420)"><span></span><span></span></div><div class="cap">Home Theater Acoustic Panels</div></div>

  <div class="abs divider" style="top:788px"><i></i></div>
</section>

<section>
  <div class="abs reasons-photo" role="img" aria-label="Dark theater room with recliners and a framed poster"></div>
  <h2 class="abs reasons-title">5 Reasons To Choose Velvet Screen For Your Home Theater</h2>
  <div class="abs reason" style="left:218px;top:858px"><h4><b>1</b>Experience Is Everything</h4><p>We have worked on over 1000 Home Theater Designs ranging from Traditional styles to modern Space Themes.</p></div>
  <div class="abs reason" style="left:356px;top:858px"><h4><b>2</b>One Size Does Not Fit All</h4><p>We have worked on over 1000 Home Theater Designs ranging from Traditional styles to modern Space Themes.</p></div>
  <div class="abs reason" style="left:498px;top:858px"><h4><b>3</b>Think Outside The Box</h4><p>We have worked on over 1000 Home Theater Designs ranging from Traditional styles to modern Space Themes.</p></div>
  <div class="abs reason" style="left:218px;top:929px"><h4><b>4</b>Size Matters</h4><p>We have worked on over 1000 Home Theater Designs ranging from Traditional styles to modern Space Themes.</p></div>
  <div class="abs reason" style="left:356px;top:929px"><h4><b>5</b>Seeing Is Believing</h4><p>We have worked on over 1000 Home Theater Designs ranging from Traditional styles to modern Space Themes.</p></div>
</section>

<footer>
  <div class="abs footer"></div>
  <div class="abs foot-col" style="left:55px;top:1045px"><h5>DESIGNS</h5><ul><li>Artesian Panels</li><li>Themes</li><li>Universal Theme</li><li>Completed Projects</li><li>Custom Theaters</li><li>Conventional Fabrics</li></ul></div>
  <div class="abs foot-col" style="left:175px;top:1045px"><h5>QUICK LINKS</h5><ul><li>Home</li><li>About us</li><li>Our Services</li><li>Getting Started</li><li>Acoustics 101</li><li>Contact us</li></ul></div>
  <div class="abs foot-col" style="left:284px;top:1045px"><h5>CUSTOMER REVIEW</h5></div>
  <div class="abs review" style="top:1068px">
    <div class="avatar"><svg width="25" height="25" viewBox="0 0 25 25"><circle cx="12.5" cy="9" r="4.5" fill="#2f2823"/><path d="M4 23c0-8 17-8 17 0z" fill="#2f2823"/></svg></div>
    <div class="name">I reviewed the summary</div>
    <p>Mara and Velvet Screen exceeded our expectations as we designed our media room with movie poster acoustical panels. The whole process was seamless.</p>
    <div class="stars">★★★<em>★★</em></div>
  </div>

  <div class="abs fold" style="left:474px;border-left:7px solid transparent"></div>
  <div class="abs fold" style="left:602px;border-right:7px solid transparent"></div>
  <div class="abs contact-box">
    <h5>CONTACT US</h5>
    <p>412 Harbor Crest Way<br>Port Linden, FL</p>
    <div class="row"><svg width="10" height="10" viewBox="0 0 16 20"><path d="M3 1l3 0 1 5-2 2c1 3 3 5 5 6l2-2 4 1 0 3c-1 2-3 2-5 1C6 15 2 10 1 5 0 3 1 1 3 1z" fill="none" stroke="#fff" stroke-width="1.5"/></svg>555-214-7730</div>
    <div class="row"><svg width="10" height="8" viewBox="0 0 10 8"><rect x=".5" y=".5" width="9" height="7" fill="none" stroke="#fff"/><path d="M.5 .5l4.5 4 4.5-4" fill="none" stroke="#fff"/></svg>hello@velvetscreen.example</div>
    <div class="socials"><span></span><span></span><span></span><span></span><span></span></div>
  </div>

  <div class="abs foot-bottom">©2014 - 2015 <b>VELVET SCREEN...</b> All Rights Reserved.</div>
</footer>

</body>
</html>
```